Hollowbrook Renderworks Wordpress Design

I would like a design for my friends company. He has just had his logo designed and really likes the following website.

www.tbr-skimcoat.co.uk

Something similar to this design would be ideal but open to additional ideas. The website shown has all the relevant content.

We have 20 years of experience and can provide a number of photos for work we have done.

More photos will be provided upon request.

Target Market(s)

Homeowners

Industry/Entity Type

Trade

Font styles to use
Sans Serif

Colors
3176b5
85cae6
85abd2
eaf1f7

Requirements
Must have
• look at www.tbr-skimcoat.co.uk
Nice to have
Should not have
• N/A

```html
<!DOCTYPE html>
<html lang="en">
<head>
<meta charset="utf-8">
<title>Hollowbrook Renderworks</title>
<link href="https://fonts.googleapis.com/css2?family=Cinzel:wght@400;700&family=Lato:ital,wght@0,400;0,700;1,400&display=swap" rel="stylesheet">
<style>
:root{
  --blue:#3176b5;
  --blue-dark:#285f94;
  --sky:#85cae6;
  --soft:#85abd2;
  --pale:#eaf1f7;
  --ink:#333;
  --grey:#8a8f96;
  --work-bg:#cdcdcd;
  --white:#fff;
}
*{box-sizing:border-box;margin:0;padding:0}
html,body{width:1200px;height:3543px;overflow:hidden}
body{font-family:"Lato",sans-serif;color:var(--ink);background:var(--white);position:relative}
section,header,footer{position:absolute;left:0;width:1200px}

/* header */
.site-header{top:0;height:145px;background:var(--white)}
.brand{position:absolute;left:85px;top:22px;width:330px}
.brand-name{font-family:"Cinzel",serif;font-weight:700;font-size:34px;color:var(--blue);line-height:1.05;letter-spacing:1px}
.brand-rule{height:3px;background:var(--blue);margin:8px 0 4px}
.brand-tag{font-size:12px;letter-spacing:5px;color:var(--blue);text-transform:uppercase}
.social{position:absolute;left:740px;top:30px;display:flex;gap:10px}
.social span{width:28px;height:28px;border-radius:50%;background:#4a4f57;display:block}
.phone{position:absolute;left:935px;top:28px;font-size:22px;display:flex;align-items:center;gap:12px;color:#222;white-space:nowrap}
.main-nav{position:absolute;right:85px;top:92px;display:flex;font-family:"Cinzel",serif;font-size:16px}
.main-nav a{color:#333;text-decoration:none;padding:0 14px;border-left:1px solid #bbb;line-height:18px}
.main-nav a:first-child{border:none;color:var(--blue);border-bottom:3px solid var(--blue);padding-bottom:8px}

/* hero */
.hero{top:145px;height:525px}
.hero-photo{position:absolute;inset:0;background:linear-gradient(100deg,#6f8fa8 0%,#4a4e52 35%,#3b3d40 60%,#2e3033 100%)}
.hero-arrow{position:absolute;top:225px;color:#fff;font-size:40px}
.callback{position:absolute;left:695px;top:95px;width:415px;height:268px;background:rgba(30,30,30,.8);border:1px solid #777;border-radius:6px;padding:0 22px}
.callback h3{font-family:"Lato",sans-serif;font-weight:700;color:#fff;font-size:16px;text-align:center;padding:15px 0;border-bottom:1px solid #666;margin:0 -22px 16px;white-space:nowrap}
.callback .field{height:30px;background:#fff;margin-bottom:14px;font-size:13px;color:#555;padding:7px 10px}
.captcha-row{display:flex;gap:12px;align-items:center}
.captcha{width:90px;color:#fff;font-weight:700;font-style:italic;letter-spacing:2px;font-size:15px}
.captcha-row .field{flex:1}
.submit-row{display:flex;align-items:center;gap:16px;margin-top:4px;color:#fff;white-space:nowrap}
.submit{background:var(--sky);color:#123;font-weight:700;font-size:17px;padding:6px 20px;border-radius:3px}
.submit-row .or{font-size:15px;font-weight:700}
.submit-row .tel{font-size:17px;font-weight:700;display:flex;align-items:center;gap:8px}
.hero-caption{position:absolute;left:0;bottom:0;width:100%;height:80px;background:rgba(20,20,20,.7);color:#fff;font-family:"Cinzel",serif;font-size:22px;text-align:center;padding-top:12px;line-height:1.35;letter-spacing:.5px}

/* section titles */
.section-title{position:absolute;left:0;width:100%;text-align:center;font-family:"Cinzel",serif;font-size:28px;color:#555;letter-spacing:1px;white-space:nowrap}
.section-title em{font-style:normal;color:var(--blue)}
.title-rule{position:absolute;height:3px;background:var(--soft)}

/* welcome */
.welcome{top:670px;height:330px}
.welcome p{position:absolute;left:95px;width:1010px;top:155px;text-align:center;font-size:14px;line-height:1.55;color:#333}
.read-more{position:absolute;left:553px;top:265px;font-size:13px;font-weight:700;color:var(--blue);border-bottom:2px solid var(--blue);padding-bottom:3px}

/* services */
.services{top:1000px;height:485px;background:var(--pale)}
.service-card{position:absolute;top:195px;width:235px;height:240px;background:#fff;border:1px solid #b9cfe4;border-bottom:3px solid var(--soft);text-align:center;padding-top:68px}
.service-card h4{font-family:"Cinzel",serif;font-weight:400;font-size:21px;color:var(--blue);letter-spacing:1px;padding-bottom:8px;border-bottom:1px solid #cfdbe8;margin:0 10px 8px;white-space:nowrap}
.service-card p{font-size:12.5px;line-height:1.45;padding:0 22px;color:#444}
.service-card .icon{position:absolute;left:67px;top:-50px;width:100px;height:100px;border-radius:50%;background:#fff;border:2px solid var(--soft);display:flex;align-items:center;justify-content:center}
.service-card.active{background:var(--blue);border-color:var(--blue);border-bottom-color:var(--sky)}
.service-card.active h4{color:#fff;border-color:#6e9ccc}
.service-card.active p{color:#fff}
.service-card.active .icon{background:var(--blue);border:4px solid #fff}
.side-arrow{position:absolute;font-size:34px;color:#777}

/* video */
.video-tips{top:1485px;height:465px}
.video-text{position:absolute;left:88px;top:175px;width:600px}
.video-text h4{color:var(--blue);font-size:19px;margin-bottom:14px}
.video-text p{font-size:14px;line-height:1.7}
.video-text .quote-link{display:inline-block;margin-top:22px;font-size:13px;font-weight:700;color:var(--blue);border-bottom:2px solid var(--blue);padding-bottom:3px;letter-spacing:.5px}
.video-player{position:absolute;left:722px;top:163px;width:383px;height:252px;background:#1c1c1c}
.video-frame{position:absolute;left:3px;top:3px;right:3px;height:210px;background:linear-gradient(90deg,#a89a86,#d8d2c7 60%,#8c8070)}
.video-bar{position:absolute;left:12px;right:12px;bottom:14px;height:4px;background:#666}
.video-bar i{display:block;width:42%;height:100%;background:var(--sky)}

/* work */
.recent-work{top:1950px;height:450px;background:var(--work-bg)}
.recent-work .sub{position:absolute;top:132px;width:100%;text-align:center;font-size:14px}
.work-photo{position:absolute;top:187px;width:242px;height:210px}
.work-photo.overlay{background:#2a3e57;color:#fff;padding:55px 28px 0}
.work-photo.overlay h5{font-size:18px;margin-bottom:10px}
.work-photo.overlay p{font-size:13px;line-height:1.5}

/* testimonials */
.testimonials{top:2400px;height:500px;background:linear-gradient(180deg,#4a86c2,#3a72aa);overflow:hidden}
.testimonials .section-title{color:#fff}
.quote-box{position:absolute;left:88px;top:145px;width:1026px;height:120px;border:1px solid #a9c7e6;border-radius:4px;color:#fff;font-style:italic;font-size:13.5px;line-height:1.6;text-align:center;padding:12px 50px}
.quote-mark{position:absolute;font-size:44px;font-family:"Cinzel",serif;color:#fff;line-height:1}
.avatar{position:absolute;left:551px;top:305px;width:98px;height:98px;border-radius:50%;border:4px solid #fff;background:linear-gradient(135deg,#c8b8a4,#8f7c6a)}
.testimonials .name{position:absolute;top:420px;width:100%;text-align:center;font-family:"Cinzel",serif;color:#fff;font-size:18px;letter-spacing:1px}
.dots{position:absolute;top:460px;width:100%;display:flex;justify-content:center;gap:8px}
.dots i{width:10px;height:10px;border-radius:50%;background:#fff;display:block}

/* partners */
.partners{top:2900px;height:272px}
.partner-row{position:absolute;left:85px;top:140px;width:1030px;display:flex;justify-content:space-between}
.partner{width:190px;height:98px;border:1px solid #c8c8c8;display:flex;align-items:center;justify-content:center}
.partner span{width:120px;height:56px;border-radius:6px;background:#dfe3e8;display:block}
.accreditation{top:3172px;height:123px;background:var(--pale)}
.accreditation h3{position:absolute;left:88px;top:32px;font-family:"Cinzel",serif;font-weight:400;font-size:25px;line-height:1.3;letter-spacing:1px;color:#222}
.accreditation .divider{position:absolute;left:410px;top:0;width:3px;height:100%;background:var(--soft)}
.accred{position:absolute;top:23px;width:205px;height:74px;background:#fff;border:1px solid #d4dce5;display:flex;align-items:center;justify-content:center}
.accred span{width:110px;height:40px;background:#dfe3e8;border-radius:4px;display:block}

/* footer */
.site-footer{top:3295px;height:248px;background:var(--blue);color:#fff}
.footer-col{position:absolute;top:18px}
.footer-col h5{font-size:14px;letter-spacing:1px;text-transform:uppercase;border-bottom:1px solid #6f9fd0;padding-bottom:7px;margin-bottom:12px;font-weight:400}
.quick-links{list-style:none;font-size:13px;line-height:29px}
.quick-links li::before{content:"";display:inline-block;width:5px;height:5px;border-radius:50%;background:#fff;margin-right:10px;vertical-align:middle}
.feed{display:flex;gap:10px;margin-bottom:16px;font-size:11px;line-height:1.4;font-style:italic}
.feed .thumb{width:52px;height:48px;background:#c9b7a2;flex:none}
.contact-line{display:flex;gap:12px;font-size:12.5px;line-height:1.45;margin-bottom:14px}
.map{width:185px;height:120px;background:linear-gradient(135deg,#e8e2c9,#cfd8bd 50%,#e2d6b8)}
.copyright{position:absolute;bottom:0;left:0;width:100%;height:43px;background:var(--blue-dark);text-align:center;font-size:12px;line-height:43px;color:#dbe7f3}
</style>
</head>
<body>

<header class="site-header">
  <div class="brand">
    <div class="brand-name">Hollowbrook<br>Renderworks</div>
    <div class="brand-rule"></div>
    <div class="brand-tag">20 years experience</div>
  </div>
  <div class="social"><span></span><span></span><span></span><span></span></div>
  <div class="phone">
    <svg width="26" height="26" viewBox="0 0 26 26"><circle cx="13" cy="13" r="11.5" fill="none" stroke="#222" stroke-width="2"/><path d="M9 7l3 3-1.5 2c1 2 2 3 4 4l2-1.5 3 3-2 2c-5 0-10.5-5.5-10.5-10.5z" fill="#222"/></svg>
    012-555-0142
  </div>
  <nav class="main-nav"><a>Home</a><a>About Us</a><a>Services</a><a>Gallery</a><a>Contact Us</a></nav>
</header>

<section class="hero">
  <div class="hero-photo" role="img" aria-label="Photo of a plasterer rendering an exterior wall with a trowel"></div>
  <span class="hero-arrow" style="left:30px">&#8249;</span>
  <span class="hero-arrow" style="right:30px">&#8250;</span>
  <form class="callback">
    <h3>Let us call you, just fill in the boxes below!</h3>
    <div class="field">Your Name</div>
    <div class="field">Your Phone Number</div>
    <div class="captcha-row"><span class="captcha">SDBGET</span><div class="field"></div></div>
    <div class="submit-row">
      <span class="submit">SUBMIT</span>
      <span class="or">Or Call Today</span>
      <span class="tel"><svg width="20" height="20" viewBox="0 0 26 26"><circle cx="13" cy="13" r="11.5" fill="none" stroke="#fff" stroke-width="2"/><path d="M9 7l3 3-1.5 2c1 2 2 3 4 4l2-1.5 3 3-2 2c-5 0-10.5-5.5-10.5-10.5z" fill="#fff"/></svg>012-555-0142</span>
    </div>
  </form>
  <div class="hero-caption">We specialise in internal plastering, rendering and thin coat insulated<br>render systems, serving both the domestic and commercial markets.</div>
</section>

<section class="welcome">
  <div class="title-rule" style="left:645px;top:40px;width:150px"></div>
  <div class="title-rule" style="left:300px;top:62px;width:600px;height:2px"></div>
  <h2 class="section-title" style="top:80px">Welcome to <em>Hollowbrook Renderworks</em></h2>
  <p>Lorem ipsum dolor sit amet, consectetuer adipiscing elit, sed diam nonummy nibh euismod tincidunt ut laoreet dolore magna aliquam erat volutpat. Ut wisi enim minim veniam, quis nostrud exerci tation ullamcorper suscipit lobortis nisl ut aliquip ex ea commodo consequat. Duis autem vel eum iriure dolor in hendrerit in vulputate velit esse molestie consequat, vel illum dolore eu feugiat nulla facilisis at vero eros et accumsan et iusto odio dignissim qui blandit praesent luptatum zzril delenit augue duis dolore te feugait nulla facilisi.</p>
  <span class="read-more">READ MORE</span>
</section>

<section class="services">
  <div class="title-rule" style="left:640px;top:40px;width:70px"></div>
  <div class="title-rule" style="left:470px;top:62px;width:260px;height:2px"></div>
  <h2 class="section-title" style="top:60px;color:#222">Our <em>Services</em></h2>
  <span class="side-arrow" style="left:38px;top:290px">&#8249;</span>
  <span class="side-arrow" style="right:38px;top:290px">&#8250;</span>

  <div class="service-card active" style="left:85px">
    <div class="icon"><svg width="50" height="50" viewBox="0 0 50 50"><path d="M12 38l16-16M30 12l8 8M22 20l8-8 8 8-8 8z" stroke="#fff" stroke-width="4" fill="none" stroke-linecap="round"/></svg></div>
    <h4>Rendering</h4>
    <p>Lorem ipsum dolor si amet the consectetur adipiscing elit Etiam feugiat urna leo Lorem ipsum is dolor si amet consectetur lorem adipiscing elit Etiam</p>
  </div>
  <div class="service-card" style="left:350px">
    <div class="icon"><svg width="50" height="50" viewBox="0 0 50 50"><rect x="12" y="12" width="26" height="26" fill="none" stroke="var(--blue)" stroke-width="3"/><path d="M18 12v26M24 12v26M30 12v26" stroke="var(--blue)" stroke-width="2"/></svg></div>
    <h4>Skimming</h4>
    <p>Lorem ipsum dolor si amet the consectetur adipiscing elit Etiam feugiat urna leo Lorem ipsum is dolor si amet consectetur lorem adipiscing elit Etiam</p>
  </div>
  <div class="service-card" style="left:617px">
    <div class="icon"><svg width="50" height="50" viewBox="0 0 50 50"><rect x="10" y="14" width="30" height="22" fill="none" stroke="var(--blue)" stroke-width="3"/><path d="M10 25h30M25 14v11M18 25v11M32 25v11" stroke="var(--blue)" stroke-width="2"/></svg></div>
    <h4>Repointing</h4>
    <p>Lorem ipsum dolor si amet the consectetur adipiscing elit Etiam feugiat urna leo Lorem ipsum is dolor si amet consectetur lorem adipiscing elit Etiam</p>
  </div>
  <div class="service-card" style="left:883px">
    <div class="icon"><svg width="50" height="50" viewBox="0 0 50 50"><path d="M10 40h30M17 40V20h16v20M21 20v-8h8v8" fill="none" stroke="var(--blue)" stroke-width="3"/></svg></div>
    <h4>Chimney Repairs</h4>
    <p>Lorem ipsum dolor si amet the consectetur adipiscing elit Etiam feugiat urna leo Lorem ipsum is dolor si amet consectetur lorem adipiscing elit Etiam</p>
  </div>
</section>

<section class="video-tips">
  <div class="title-rule" style="left:665px;top:40px;width:150px"></div>
  <div class="title-rule" style="left:255px;top:62px;width:690px;height:2px"></div>
  <h2 class="section-title" style="top:70px;color:#8a8f96">Hollowbrook <em>Renderworks's Monthly Video Tips</em></h2>
  <div class="video-text">
    <h4>Introduction into Re-pointing</h4>
    <p>Lorem ipsum dolor si amet the consectetur adipiscing elit Etiam feugiat urna leo Lorem ipsum is dolor si amet consectetur lorem adipiscing elit the is the EtiamLorem ipsum dolor si amet the consectetur adipiscing elit Etiam feugiat urna leo Lorem ipsum is dolor si amet consectetur lorem adipiscing elit lorem EtiamLorem ipsum dolor si amet the consectetur adipiscing elit Etiam.</p>
    <span class="quote-link">CONTACT US TODAY FOR A FREE QUOTE</span>
  </div>
  <div class="video-player">
    <div class="video-frame" role="img" aria-label="Video still of a plasterer working in an unfinished room"></div>
    <svg style="position:absolute;left:160px;top:80px" width="60" height="44" viewBox="0 0 60 44"><rect width="60" height="44" rx="6" fill="rgba(0,0,0,.7)"/><path d="M24 12l14 10-14 10z" fill="#fff"/></svg>
    <div class="video-bar"><i></i></div>
  </div>
</section>

<section class="recent-work">
  <h2 class="section-title" style="top:88px;color:#222">Hollowbrook <em>Renderworks's Recent Work?</em></h2>
  <p class="sub">Lorem ipsum dolor sit amet, consectetuer adipiscing elit, sed diam nonummy nibh euismod tincidunt ut laoreet dolore</p>
  <span class="side-arrow" style="left:38px;top:245px">&#8249;</span>
  <span class="side-arrow" style="right:38px;top:245px">&#8250;</span>
  <div class="work-photo" style="left:85px;background:linear-gradient(160deg,#e6e2da,#a88e72)" role="img" aria-label="Photo of a rendered house front with bay window"></div>
  <div class="work-photo overlay" style="left:347px">
    <h5>Lorem ipsum dolor</h5>
    <p>Lorem ipsum dolor si amet the consectetur adipiscing elit Etiam feugiat urna leo.</p>
  </div>
  <div class="work-photo" style="left:610px;background:linear-gradient(180deg,#b9d3ec,#c8c0a0 55%,#5f8a48)" role="img" aria-label="Photo of a finished two-storey house with lawn"></div>
  <div class="work-photo" style="left:873px;background:linear-gradient(170deg,#a9c4de,#9a7458 45%,#6b4c38)" role="img" aria-label="Photo of a stone-faced house with porch"></div>
</section>

<section class="testimonials" role="img" aria-label="Faded background photo of a happy family outside their home">
  <div class="title-rule" style="left:640px;top:40px;width:70px;background:#bcd3ea"></div>
  <div class="title-rule" style="left:410px;top:62px;width:380px;height:2px;background:#bcd3ea"></div>
  <h2 class="section-title" style="top:75px">Client Testimonials</h2>
  <div class="quote-box">Lorem ipsum dolor sit amet, consectetuer adipiscing elit, sed diam nonummy nibh euismod tincidunt ut laoreet dolore magna aliquam erat volutpat. Ut wisi enim minim veniam, quis nostrud exerci tation ullamcorper suscipit lobortis nisl ut aliquip ex ea commodo consequat. Dolore eu feugiat nulla facilisis at vero eros et accumsan et iusto odio dignissim qui blandit praesent luptatum.</div>
  <span class="quote-mark" style="left:92px;top:150px">&ldquo;</span>
  <span class="quote-mark" style="left:870px;top:225px">&rdquo;</span>
  <svg style="position:absolute;left:585px;top:264px" width="30" height="16" viewBox="0 0 30 16"><path d="M0 0l15 15L30 0" fill="#3f7ab4" stroke="#a9c7e6"/></svg>
  <div class="avatar" role="img" aria-label="Client portrait"></div>
  <div class="name">Lorem Ipsum</div>
  <div class="dots"><i></i><i></i><i></i></div>
</section>

<section class="partners">
  <div class="title-rule" style="left:690px;top:40px;width:150px"></div>
  <div class="title-rule" style="left:150px;top:62px;width:900px;height:2px"></div>
  <h2 class="section-title" style="top:60px;color:#222">We are proud to be <em>working with the following Companies</em></h2>
  <span class="side-arrow" style="left:38px;top:165px">&#8249;</span>
  <span class="side-arrow" style="right:38px;top:165px">&#8250;</span>
  <div class="partner-row">
    <div class="partner"><span></span></div>
    <div class="partner"><span></span></div>
    <div class="partner"><span></span></div>
    <div class="partner"><span></span></div>
    <div class="partner"><span></span></div>
  </div>
</section>

<section class="accreditation">
  <h3>Accreditation and<br>Memberships</h3>
  <div class="divider"></div>
  <div class="accred" style="left:448px"><span></span></div>
  <div class="accred" style="left:673px"><span></span></div>
  <div class="accred" style="left:898px"><span></span></div>
</section>

<footer class="site-footer">
  <div class="footer-col" style="left:88px;width:150px">
    <h5>Quick Links</h5>
    <ul class="quick-links"><li>Home</li><li>About Us</li><li>Services</li><li>Gallery</li><li>Contact Us</li></ul>
  </div>
  <div class="footer-col" style="left:258px;width:300px">
    <h5>Chirpline Feeds <span style="float:right;font-size:12px;text-decoration:underline;text-transform:none">View All</span></h5>
    <div class="feed"><div class="thumb" role="img" aria-label="Profile photo"></div><div>Lorem ipsum is simply dummy short post http://hb.example/post56<br>12 minutes ago</div></div>
    <div class="feed"><div class="thumb" role="img" aria-label="Profile photo"></div><div>Lorem ipsum is simply dummy short post http://hb.example/post56<br>9 minutes ago</div></div>
  </div>
  <div class="footer-col" style="left:618px;width:250px">
    <h5>Contact Details</h5>
    <div class="contact-line"><svg width="14" height="20" viewBox="0 0 14 20"><path d="M7 0a7 7 0 0 1 7 7c0 5-7 13-7 13S0 12 0 7a7 7 0 0 1 7-7z" fill="#fff"/><circle cx="7" cy="7" r="2.5" fill="var(--blue)"/></svg><div>Loren Street No 5261 lorem ipsum<br>Near wall street optisilho dolor Smt<br>nonumy - 334687</div></div>
    <div class="contact-line"><svg width="16" height="16" viewBox="0 0 26 26"><path d="M6 3l5 5-2.5 3c1.5 3 3.5 5 6.5 6.5l3-2.5 5 5-3 3C11 23 3 15 3 6z" fill="#fff"/></svg>012-555-0142</div>
    <div class="contact-line"><svg width="16" height="12" viewBox="0 0 16 12"><rect width="16" height="12" fill="#fff"/><path d="M0 0l8 7 8-7" fill="none" stroke="var(--blue)" stroke-width="1.5"/></svg>info@hollowbrook-render.com</div>
  </div>
  <div class="footer-col" style="left:920px;width:190px">
    <h5>Location Map</h5>
    <div class="map" role="img" aria-label="Street map showing the office location"></div>
  </div>
  <div class="copyright">Copyright &copy; 2016 Hollowbrook Renderworks. All Rights Reserved</div>
</footer>

</body>
</html>
```